2018 Fundraiser Event Flier

We are a non profit that works in the homeless community, The Lanternwick Guild. We offer a unique program of supported employment that is all about community engagement and building relationships not only with our participants but with community businesses and non profit partners. Our mission statement is "We seek and foster partnerships between the business and nonprofit communities to respectfully and effectively guide individuals from disenfranchised communities forward in sustainable employment to realize their potential of fully enriched lives for themselves and their families" We are having a fundraising event on Dec 13 and need a flier to advertise the event both via email and physical postings. We like a black background and bright colors (see uploaded example) and want to advertise the event and a small amount about who we are. Fun and bright. We will upload two of our logos and two photos that we have used in branding previously.

```html
<!DOCTYPE html>
<html lang="en">
<head>
<meta charset="utf-8">
<title>The Lanternwick Guild – Fundraising Event Flier</title>
<link rel="stylesheet" href="https://fonts.googleapis.com/css2?family=Bebas+Neue&family=Open+Sans:wght@400;600;700&display=swap">
<style>
  :root {
    --stage: #e9e7e4;
    --paper: #ffffff;
    --ink-band: #221f20;
    --ink-dark: #231f20;
    --photo-light: #9a9a9a;
    --photo-dark: #3c3c3c;
    --accent: #f07f22;
    --text-light: #ffffff;
    --rule: #6a6a6a;
  }
  * { box-sizing: border-box; margin: 0; padding: 0; }
  html, body {
    width: 1046px;
    height: 1200px;
    overflow: hidden;
    background: var(--stage);
  }
  .flier {
    position: absolute;
    left: 58px;
    top: 0;
    width: 930px;
    height: 1200px;
    background: var(--paper);
    overflow: hidden;
    font-family: "Open Sans", Arial, sans-serif;
  }
  .flier__photo {
    position: absolute;
    left: 0; top: 0;
    width: 930px; height: 470px;
    background: radial-gradient(ellipse at 42% 40%, var(--photo-light) 0%, #7a7a7a 40%, var(--photo-dark) 100%);
  }
  .flier__band {
    position: absolute;
    left: 0; top: 0;
    width: 930px; height: 1200px;
  }
  .headline {
    position: absolute;
    top: 502px; left: 0; width: 100%;
    text-align: center;
    font-family: "Bebas Neue", Impact, sans-serif;
    font-size: 50px;
    letter-spacing: 0.5px;
    color: var(--text-light);
    line-height: 1;
  }
  .offer {
    position: absolute;
    top: 582px; left: 0; width: 100%;
    text-align: center;
    font-weight: 700;
    font-size: 20px;
    line-height: 30px;
    color: var(--accent);
  }
  .section-label {
    position: absolute;
    height: 30px;
    width: 270px;
    background: var(--accent);
    clip-path: polygon(2% 18%, 20% 6%, 45% 12%, 70% 2%, 96% 8%, 100% 30%, 97% 62%, 100% 92%, 74% 100%, 48% 88%, 22% 98%, 0% 86%, 4% 56%);
    color: var(--text-light);
    font-weight: 700;
    font-size: 18px;
    line-height: 30px;
    padding-left: 36px;
    text-transform: uppercase;
  }
  .section-label--about { top: 675px; left: 45px; }
  .section-label--mission { top: 830px; left: 45px; }
  .section-text {
    position: absolute;
    color: var(--text-light);
    font-size: 14.5px;
    line-height: 23px;
  }
  .section-text--about { top: 722px; left: 80px; width: 836px; }
  .section-text--mission { top: 872px; left: 11px; width: 905px; }
  .section-rule {
    position: absolute;
    top: 815px; left: 60px;
    width: 690px;
    border-top: 2px dotted var(--rule);
  }
  .org-name {
    position: absolute;
    left: 30px; top: 1090px;
    width: 320px;
    font-weight: 700;
    font-size: 34px;
    line-height: 40px;
    color: var(--ink-dark);
  }
  .venue {
    position: absolute;
    right: 103px; top: 1116px;
    text-align: right;
    font-size: 15px;
    line-height: 22px;
    color: var(--ink-dark);
  }
  .venue__name { color: var(--accent); }
  .venue-mark {
    position: absolute;
    left: 842px; top: 1110px;
    width: 70px; height: 70px;
    border-radius: 50%;
    background: #8a8a8a;
  }
</style>
</head>
<body>
  <main class="flier">
    <div class="flier__photo" role="img" aria-label="Black and white photograph of a man in a knit cap holding a cardboard sign reading Willing to Work, seated beside his bags"></div>

    <svg class="flier__band" viewBox="0 0 930 1200" aria-hidden="true">
      <polygon fill="var(--paper)" points="0,372 38,368 72,380 104,377 142,385 178,381 216,391 252,388 288,398 332,394 368,404 412,400 448,411 492,407 528,417 572,413 608,424 652,420 688,431 732,427 768,437 812,433 848,444 892,441 930,447 930,470 0,470"/>
      <polygon fill="var(--ink-band)" points="0,382 40,378 70,390 105,386 140,395 180,392 215,401 250,398 290,408 330,404 370,414 410,411 450,420 490,417 530,427 570,424 610,434 650,430 690,441 730,437 770,447 810,444 850,454 890,451 930,458 930,940 895,946 860,938 820,949 785,944 745,954 705,948 668,958 630,952 590,962 550,956 512,966 470,960 432,970 392,963 352,973 312,967 272,976 232,970 192,979 152,973 112,982 72,976 34,985 0,978"/>
    </svg>

    <h1 class="headline">Fundraising Event on Dec 13</h1>
    <p class="offer">Enjoy a pizza at Casa Brasa Pizzeria + Taqueria in the month of December<br>and 1% of all sales supports the lanternwick guild</p>

    <h2 class="section-label section-label--about">About us</h2>
    <p class="section-text section-text--about">We are a non profit that works in the homeless community, The Lanternwick Guild. We offer a unique program of supported employment that is all about community engagement and building relationships not only with our participants but with community businesses and non profit partners.</p>

    <div class="section-rule"></div>

    <h2 class="section-label section-label--mission">Mission statement</h2>
    <p class="section-text section-text--mission">We seek and foster partnerships between the business and nonprofit communities to respectfully and effectively guide individuals from disenfranchised communities forward in sustainable employment to realize their potential of fully enriched lives for themselves and their families</p>

    <p class="org-name">The Lanternwick Guild</p>

    <address class="venue">
      <span class="venue__name">Casa Brasa Pizzeria + Taqueria</span><br>
      2871 Marlow Street<br>
      Denver, CO 80219
    </address>
    <div class="venue-mark" aria-hidden="true"></div>
  </main>
</body>
</html>
```